Business Card Design

​Silver Harbor Grooves provides personal, friendly service in a fun and high energy environment. We are based in Vermont.

We would like a card that appeals to a wide range of audiences as we do a wide range of events. Please feel free to check out our website silverharborgrooves.com for inspiration.

Target Market(s)

weddings, corporate, birthday parties, colleges

Industry/Entity Type

Business

Contact Information for Business Card

Silver Harbor Grooves
Providing Entertainment For All Occasions
555 218 6093
silverharborgrooves@mailvane.com
silverharborgrooves.com

```html
<!DOCTYPE html>
<html lang="en">
<head>
<meta charset="utf-8">
<title>Silver Harbor Grooves — Business Cards</title>
<link href="https://fonts.googleapis.com/css2?family=Open+Sans:wght@400;600;700&display=swap" rel="stylesheet">
<style>
  :root {
    --page: #e9e6e1;
    --card: #ffffff;
    --green: #2d5a1b;
    --green-faint: #d9e3d3;
    --red: #9c1f1f;
    --ink: #3a3a3a;
    --ink-soft: #555555;
    --shadow: rgba(0,0,0,0.18);
  }
  * { box-sizing: border-box; margin: 0; padding: 0; }
  html, body {
    width: 1200px; height: 829px; overflow: hidden;
    background: var(--page);
    font-family: "Open Sans", Arial, sans-serif;
  }
  .stage {
    width: 1200px; height: 829px;
    display: flex; align-items: center; justify-content: center; gap: 60px;
  }
  .card {
    position: relative;
    width: 530px; height: 303px;
    background: var(--card);
    box-shadow: 0 6px 18px var(--shadow);
  }

  /* Contact side */
  .brand-name {
    font-weight: 700; color: var(--green);
    letter-spacing: 0.02em; text-transform: uppercase;
    display: flex; align-items: center; gap: 10px;
  }
  .brand-mark {
    width: 14px; height: 14px; background: var(--red);
  }
  .contact-side .brand-name {
    position: absolute; left: 34px; top: 58px; font-size: 17px;
  }
  .contact-list {
    position: absolute; left: 34px; top: 118px;
    list-style: none; font-size: 13px; color: var(--ink);
  }
  .contact-list li {
    display: flex; align-items: center; gap: 8px; height: 22px;
  }
  .contact-list svg { width: 13px; height: 13px; flex: none; }
  .address {
    position: absolute; left: 34px; bottom: 40px;
    font-size: 13px; color: var(--ink);
  }
  .holder {
    position: absolute; right: 34px; top: 44px; text-align: right;
  }
  .holder-name { font-size: 15px; font-weight: 700; color: var(--green); }
  .holder-title { font-size: 11px; color: var(--ink-soft); }
  .faint-brand {
    position: absolute; right: 34px; top: 92px;
    font-size: 15px; font-weight: 700; color: var(--green-faint);
    text-transform: uppercase; letter-spacing: 0.02em;
  }

  /* Logo side */
  .logo-side {
    display: flex; flex-direction: column; align-items: center; justify-content: center;
  }
  .logo-side .brand-name { font-size: 26px; }
  .logo-side .brand-mark { width: 20px; height: 20px; }
  .website {
    margin-top: 28px; font-size: 16px; color: var(--ink); letter-spacing: 0.04em;
  }
</style>
</head>
<body>
<main class="stage">
  <section class="card contact-side">
    <div class="brand-name"><span class="brand-mark"></span>Silver Harbor Grooves</div>

    <ul class="contact-list">
      <li>
        <svg viewBox="0 0 16 16"><circle cx="8" cy="8" r="8" fill="var(--green)"/><path d="M5 4.5l1.6-.5 1 2.2-1 .8c.5 1 1.2 1.7 2.2 2.2l.8-1 2.2 1-.5 1.6C8.6 11 5 7.4 5 4.5z" fill="#fff"/></svg>
        555 218 6093
      </li>
      <li>
        <svg viewBox="0 0 16 16"><circle cx="8" cy="8" r="8" fill="var(--green)"/><rect x="4" y="5.5" width="8" height="5.5" fill="#fff"/><path d="M4 5.5l4 3 4-3" stroke="var(--green)" stroke-width="0.9" fill="none"/></svg>
        silverharborgrooves@mailvane.com
      </li>
      <li>
        <svg viewBox="0 0 16 16"><circle cx="8" cy="8" r="8" fill="var(--green)"/><circle cx="8" cy="8" r="4.2" stroke="#fff" fill="none"/><path d="M3.8 8h8.4M8 3.8c-2 2.6-2 5.8 0 8.4M8 3.8c2 2.6 2 5.8 0 8.4" stroke="#fff" stroke-width="0.8" fill="none"/></svg>
        www.silverharborgrooves.com
      </li>
    </ul>

    <p class="address">Street Name, City Name, Zip Code-00000</p>

    <div class="holder">
      <p class="holder-name">Your Name</p>
      <p class="holder-title">Title</p>
    </div>
    <div class="faint-brand">Silver Harbor Grooves</div>
  </section>

  <section class="card logo-side">
    <div class="brand-name"><span class="brand-mark"></span>Silver Harbor Grooves</div>
    <p class="website">www.silverharborgrooves.com</p>
  </section>
</main>
</body>
</html>
```